Award-winnning Estate Agent needs a premium version of their 'For Sale' board design

We need a premium option for our 'For Sale' board design. We have a standard board that is attached to this brief, but were are looking to have a premium design version that we will use when selling exclusive properties. Our company name is Harbour Lane Estates and the name for this is exclusive selection is: 'The Harbour Collection'. The design needs to work with our current brand, but have a distinctive PREMIUM feel to it. I have uploaded the barnd guidelines and also some of the exisisting logo variations. We do NOT need a new logo but feel free to play around with colours, fonts, sizes etc. for the sign.

Target Market(s)

Property buyers & house hunters

Industry/Entity Type

Real Estate - Residential Property

Font styles to use
Sans Serif

Requirements
Must have
• A premium fee, must be square design, must be easy to read when driving past the sign
Nice to have
• I'm open ot ideas

```html
<!DOCTYPE html>
<html lang="en">
<head>
<meta charset="UTF-8">
<title>Harbour Lane Estates – The Harbour Collection For Sale Board</title>
<link rel="stylesheet" href="https://fonts.googleapis.com/css2?family=Arimo:wght@400;700&display=swap">
<style>
  :root {
    --backdrop-light: #f2f2f2;
    --backdrop-dark: #b9b9b9;
    --board-frame: #e6e8e8;
    --brand-blue: #2ea9e1;
    --brand-purple: #373083;
    --panel-white: #ffffff;
    --text-dark: #1d1d1f;
    --keyline: rgba(255, 255, 255, 0.55);
  }
  * { box-sizing: border-box; margin: 0; padding: 0; }
  html, body {
    width: 916px;
    height: 1200px;
    overflow: hidden;
  }
  body {
    background: linear-gradient(100deg, var(--backdrop-light) 0%, #d8d8d8 55%, var(--backdrop-dark) 100%);
    font-family: "Arimo", Arial, sans-serif;
    position: relative;
  }
  .sale-board {
    position: absolute;
    left: 78px;
    top: 220px;
    width: 760px;
    height: 760px;
    background: var(--board-frame);
    padding: 20px;
    display: flex;
    flex-direction: column;
  }
  .brand-panel {
    position: relative;
    height: 372px;
    background: var(--brand-blue);
    display: flex;
    flex-direction: column;
    align-items: center;
    justify-content: flex-end;
    padding-bottom: 52px;
  }
  .brand-panel::before {
    content: "";
    position: absolute;
    inset: 14px 14px 0 14px;
    border: 2px solid var(--keyline);
    border-bottom: none;
    pointer-events: none;
  }
  .collection-label {
    display: flex;
    align-items: center;
    gap: 18px;
    color: var(--panel-white);
    font-weight: 400;
    font-size: 26px;
    letter-spacing: 7px;
    text-transform: uppercase;
    margin-bottom: 70px;
  }
  .collection-label::before,
  .collection-label::after {
    content: "";
    width: 60px;
    height: 2px;
    background: var(--panel-white);
  }
  .brand-line {
    display: flex;
    align-items: center;
    gap: 16px;
  }
  .brand-mark {
    width: 36px;
    height: 36px;
    background: var(--panel-white);
  }
  .brand-name {
    color: var(--panel-white);
    font-weight: 700;
    font-size: 52px;
    line-height: 1;
    letter-spacing: -0.5px;
  }
  .status-band {
    height: 150px;
    background: var(--brand-purple);
    display: flex;
    align-items: center;
    justify-content: center;
  }
  .status-label {
    color: var(--panel-white);
    font-weight: 700;
    font-size: 120px;
    letter-spacing: 3px;
    line-height: 1;
  }
  .contact-panel {
    flex: 1;
    background: var(--panel-white);
    display: flex;
    flex-direction: column;
    align-items: center;
    justify-content: center;
    padding-top: 4px;
  }
  .contact-phone {
    color: var(--brand-purple);
    font-size: 92px;
    line-height: 1;
    letter-spacing: -1px;
  }
  .contact-web {
    margin-top: 8px;
    color: var(--text-dark);
    font-size: 36px;
    line-height: 1;
  }
  .contact-web .web-name { color: var(--brand-blue); }
</style>
</head>
<body>
  <main class="sale-board">
    <section class="brand-panel">
      <p class="collection-label">The Harbour Collection</p>
      <div class="brand-line">
        <span class="brand-mark"></span>
        <span class="brand-name">Harbour Lane Estates</span>
      </div>
    </section>
    <section class="status-band">
      <h1 class="status-label">FOR SALE</h1>
    </section>
    <section class="contact-panel">
      <p class="contact-phone">01632 960482</p>
      <p class="contact-web">www.<span class="web-name">harbourlaneestates</span>.co.uk</p>
    </section>
  </main>
</body>
</html>
```